Business Card Design

5* Hotel Property based on an island in Greece

My position is aparta from being a director, i'm on the accounts payable too, not sure how this should be stated, with a comma or "/"?

Sorry about the uploaded logo, it was a mistaken one!

There's also need to be added this  www.corvanteholdings.com on the back side of the card!

Also need to have the logo of the corvante holdings which can be found in a second on the brief! Thank you guys, irini

Industry/Entity Type

Business

Contact Information for Business Card

VERISTOKA PELLA Hotel
Irini Dravetsou
Director, AP Dept.

www.veristoka.gr
Peltira Island 85300
Greece

irinidravetsou@fenmail.com
+306951273064

```html
<!DOCTYPE html>
<html lang="en">
<head>
<meta charset="utf-8">
<title>Veristoka Pella Hotel – Business Card</title>
<link rel="stylesheet" href="https://fonts.googleapis.com/css2?family=Lato:wght@300;400&display=swap">
<style>
  :root {
    --page-bg: #dff1fa;
    --card-white: #ffffff;
    --band-blue: #0d93d8;
    --band-deep: #0a6cc2;
    --band-line: rgba(255,255,255,0.35);
    --ink-grey: #4a4a4a;
    --ink-soft: #8a8f94;
    --brand-blue: #1a8fd8;
    --shadow: rgba(20,80,120,0.25);
  }
  * { margin: 0; padding: 0; box-sizing: border-box; }
  html, body {
    width: 1200px; height: 1071px; overflow: hidden;
    background: var(--page-bg);
    font-family: "Lato", sans-serif;
  }
  .canvas {
    position: relative; width: 1200px; height: 1071px;
  }
  .card {
    position: absolute; left: 250px;
    width: 700px; height: 400px;
    background: var(--card-white);
    border-radius: 28px;
    overflow: hidden;
    box-shadow: 0 10px 30px var(--shadow);
  }
  .card--back { top: 85px; }
  .card--front { top: 575px; }

  .band {
    position: absolute; left: 0; right: 0;
    background: radial-gradient(ellipse at 55% 60%, var(--band-deep) 0%, var(--band-blue) 60%);
  }
  .band::before, .band::after {
    content: ""; position: absolute; left: 0; right: 0;
    height: 1px; background: var(--band-line);
  }
  .band::before { top: 8px; }
  .band::after { bottom: 8px; }

  .card--back .band { top: 130px; height: 140px; }
  .card--front .band { top: 125px; height: 145px; }

  .brand {
    position: absolute; display: flex; align-items: center; gap: 14px;
  }
  .brand__dot {
    width: 62px; height: 62px; border-radius: 50%;
    background: var(--brand-blue);
    flex: none;
  }
  .brand__name {
    font-weight: 300; font-size: 30px; letter-spacing: 0.5px;
    text-transform: uppercase; line-height: 1;
  }
  .card--back .brand { left: 110px; top: 168px; }
  .card--back .brand__dot { background: #bfe3f7; }
  .card--back .brand__name { color: #ffffff; }
  .card--front .brand { left: 30px; top: 30px; }
  .card--front .brand__name { color: var(--ink-soft); }

  .back-web {
    position: absolute; left: 0; right: 0; top: 300px;
    text-align: center; font-size: 18px; font-weight: 400;
    color: var(--ink-grey);
  }

  .holder {
    position: absolute; right: 34px; top: 200px;
    text-align: right; color: #ffffff;
  }
  .holder__name { font-size: 32px; font-weight: 300; line-height: 1.1; }
  .holder__title { font-size: 14px; font-weight: 400; margin-top: 4px; }

  .address {
    position: absolute; left: 34px; top: 298px;
    font-size: 17px; line-height: 1.35; color: var(--ink-grey);
  }
  .contact {
    position: absolute; left: 350px; top: 312px;
    display: grid; grid-template-columns: 66px auto; row-gap: 2px;
    font-size: 17px; color: var(--ink-grey);
  }
</style>
</head>
<body>
<main class="canvas">

  <section class="card card--back" aria-label="Card back">
    <div class="band"></div>
    <div class="brand">
      <span class="brand__dot"></span>
      <span class="brand__name">Veristoka Pella Hotel</span>
    </div>
    <p class="back-web">www.veristoka.gr</p>
  </section>

  <section class="card card--front" aria-label="Card front">
    <div class="brand">
      <span class="brand__dot"></span>
      <span class="brand__name">Veristoka Pella Hotel</span>
    </div>
    <div class="band"></div>
    <div class="holder">
      <p class="holder__name">Irini Dravetsou</p>
      <p class="holder__title">Director, AP Dept.</p>
    </div>
    <address class="address" style="font-style:normal">
      VERISTOKA PELLA Hotel<br>
      Peltira Island 85300, Greece
    </address>
    <div class="contact">
      <span>E-mail:</span><span>irinidravetsou@fenmail.com</span>
      <span>Call:</span><span>+306951273064</span>
    </div>
  </section>

</main>
</body>
</html>
```